Hearthside Pots: A Patient Palate's Companion

Hi, I had a book cover designed on this site, but I want to modify the cover and change the colours. I want to keep the slow cooker and the ingredients on the cover, but I want to simplify it a bit. And, I am open to other ideas. I have attached below a book cover idea I like and I like the colors as well. I want it to be called Hearthside Pots, with the language on the right corner: "Curated For Nearly Effortless Meals That Are Greater Than The Sum Of Their Ingredients" I like the circles idea and my name as the author on the curve.

Target Market(s)

Home Cooks

Colors
00AB8E
00BBA5
67D7C9
C6EFE9
E9F9F6
F0912C
F2A743
F7CA91
FBE8D2
FDF5EE
E54698
E96AAD
F1A4CE
F9D9EA
FCEFF6
6B429C
8869AF
B7A5CE
E3DAEB
F3F0F8

Requirements
Must have
• Please use the colors on the Marigold Table Recipe Book and I like the design, but I do not want it identical. I like the author name (Harold P. Quimby) on the side of the circle on the upper right side of the cover.
Nice to have
• I like the large words "Hearthside Pots"

```html
<!DOCTYPE html>
<html lang="en">
<head>
<meta charset="utf-8">
<title>Hearthside Pots – Book Cover</title>
<link rel="stylesheet" href="https://fonts.googleapis.com/css2?family=Cinzel:wght@400;700&display=swap">
<style>
  :root {
    --field-teal: #00ab8e;
    --cream: #fdf5ee;
    --marigold: #f2a743;
    --orange: #f0912c;
    --apricot: #f7ca91;
    --rose: #e96aad;
    --magenta: #e54698;
    --aqua: #67d7c9;
    --plum: #8869af;
    --deep-plum: #6b429c;
    --mist: #e3daeb;
    --lavender: #b7a5ce;
    --ink: #0b0b0b;
    --paper: #ffffff;
  }
  html, body {
    margin: 0;
    padding: 0;
    width: 746px;
    height: 1200px;
    overflow: hidden;
    background: var(--field-teal);
  }
  .cover {
    position: relative;
    width: 746px;
    height: 1200px;
    overflow: hidden;
    background: var(--field-teal);
    font-family: "Cinzel", "Times New Roman", serif;
  }
  .cover-art {
    position: absolute;
    inset: 0;
  }
  .circle-blend { mix-blend-mode: multiply; }

  .title {
    position: absolute;
    left: 0;
    width: 614px;
    top: 292px;
    margin: 0;
    text-align: center;
    font-weight: 700;
    color: var(--ink);
    line-height: 1;
    font-variant: small-caps;
    text-shadow: 0 0 14px rgba(255,255,255,0.95), 0 0 4px rgba(255,255,255,0.9);
  }
  .title-line {
    display: block;
    font-size: 104px;
    letter-spacing: 1px;
  }

  .tagline {
    position: absolute;
    left: 262px;
    top: 702px;
    width: 446px;
    margin: 0;
    text-align: center;
    color: var(--paper);
    font-size: 20px;
    line-height: 1.32;
    font-variant: small-caps;
    letter-spacing: 0.2px;
    text-shadow: 0 1px 2px rgba(0,0,0,0.4);
  }

  .photo { position: absolute; }
  .photo--spice-top-left {
    left: 0; top: 0; width: 118px; height: 150px;
    border-radius: 0 0 64px 0;
    background: linear-gradient(150deg, var(--orange), var(--apricot));
  }
  .photo--produce-top-right {
    left: 478px; top: 0; width: 268px; height: 330px;
    border-radius: 0 0 0 150px;
    background: linear-gradient(200deg, var(--cream) 0%, var(--apricot) 45%, var(--marigold) 100%);
  }
  .photo--pepper-left {
    left: 0; top: 612px; width: 36px; height: 128px;
    border-radius: 0 36px 36px 0;
    background: var(--orange);
  }
  .photo--tomato-left {
    left: 0; top: 792px; width: 116px; height: 108px;
    border-radius: 0 54px 54px 0;
    background: var(--magenta);
  }
  .photo--produce-bottom-right {
    left: 396px; top: 906px; width: 350px; height: 294px;
    border-radius: 160px 0 0 0;
    background: linear-gradient(160deg, var(--magenta) 0%, var(--orange) 60%, var(--apricot) 100%);
  }
  .photo--cooker {
    left: 0; top: 958px; width: 286px; height: 242px;
    border-radius: 70px 90px 0 0;
    background: linear-gradient(180deg, var(--lavender) 0%, var(--mist) 30%, #f7f5fa 100%);
  }
</style>
</head>
<body>
<main class="cover">
  <svg class="cover-art" width="746" height="1200" viewBox="0 0 746 1200" aria-hidden="true">
    <circle cx="448" cy="576" r="500" fill="var(--cream)"/>
    <circle class="circle-blend" cx="448" cy="267" r="160" fill="var(--marigold)"/>
    <circle class="circle-blend" cx="740" cy="355" r="165" fill="var(--rose)"/>
    <circle class="circle-blend" cx="290" cy="620" r="267" fill="var(--aqua)"/>
    <circle class="circle-blend" cx="600" cy="855" r="270" fill="var(--plum)"/>
    <defs>
      <path id="author-arc" d="M 66 262 A 470 470 0 0 1 330 60"/>
    </defs>
    <text class="author-name" font-family="Cinzel, serif" font-size="27" fill="#ffffff" letter-spacing="2">
      <textPath href="#author-arc" startOffset="4">Harold P. Quimby</textPath>
    </text>
  </svg>

  <div class="photo photo--spice-top-left" role="img" aria-label="Dried chillies and an orange slice"></div>
  <div class="photo photo--produce-top-right" role="img" aria-label="Squash, lemons, pomegranate seeds and a bowl of chickpeas"></div>
  <div class="photo photo--pepper-left" role="img" aria-label="Roasted pepper"></div>
  <div class="photo photo--tomato-left" role="img" aria-label="Ripe tomato on the vine"></div>
  <div class="photo photo--produce-bottom-right" role="img" aria-label="Tomatoes, orange slices, spices and a bowl of sauce"></div>
  <div class="photo photo--cooker" role="img" aria-label="White slow cooker with glass lid"></div>

  <h1 class="title">
    <span class="title-line">Hearthside</span>
    <span class="title-line">Pots</span>
  </h1>

  <p class="tagline">Curated For Nearly Effortless Meals That Are Greater Than The Sum Of Their Ingredients</p>
</main>
</body>
</html>
```